Every Road Meets Home needs a canvas shopping bag design

Dear Designers,
I have a registered Trade Mark Logo that I want incorporated on a canvas shopping bag “Every Road Meets Home” One side will have the logo and added design to compliment it and the other side is going to be quotes from everyday people ( you and I :º) I will provide the first quote but will need the final design to allow me to change that quote i.e. psd. Please add design to compliment the quotes.
The quote should say “There is only one race the human race and we all belong to it.” Walt WWII Combat vet ex POW….1964.

I look forward to seeing your designs and I hope the quote itself inspires you.

Thanks,
Joy

Target Market(s)

Consumers, stores....

Industry/Entity Type

Shopping

Font styles to use
Script

Requirements
Must have
• Room for content, also a handwritten font but not fancy.
Nice to have
• Something universal that resonates with all human beings.
Should not have
• Nothing religious or political that would alienate anyone one.

```html
<!DOCTYPE html>
<html lang="en">
<head>
<meta charset="utf-8">
<title>Every Road Meets Home — Quote Tote</title>
<link rel="stylesheet" href="https://fonts.googleapis.com/css2?family=Federo&display=swap">
<style>
  :root {
    --canvas-natural: #ece2cc;
    --ink: #111111;
    --rule-colour: #2fa9c8;
    --mark-teal: #1f8fa6;
  }
  html, body {
    margin: 0;
    padding: 0;
    width: 1200px;
    height: 1200px;
    overflow: hidden;
    background: var(--canvas-natural);
  }
  .tote-print {
    position: relative;
    width: 1200px;
    height: 1200px;
    font-family: "Federo", sans-serif;
    color: var(--ink);
  }
  .quote-line {
    position: absolute;
    left: 0;
    width: 1180px;
    margin: 0;
    text-align: center;
    font-size: 72px;
    font-weight: 400;
    line-height: 1;
    letter-spacing: -1.5px;
    white-space: nowrap;
  }
  .quote-line--first  { top: 524px; }
  .quote-line--second { top: 622px; }
  .quote-line--third  { top: 718px; }
  .quote-rule {
    position: absolute;
    left: 248px;
    width: 687px;
    height: 3px;
    background: var(--rule-colour);
  }
  .quote-rule--upper { top: 606px; }
  .quote-rule--lower { top: 707px; }
  .brand-lockup {
    position: absolute;
    left: 0;
    top: 920px;
    width: 1170px;
    display: flex;
    justify-content: center;
    align-items: center;
    gap: 14px;
  }
  .brand-dot {
    width: 34px;
    height: 34px;
    border-radius: 50%;
    background: var(--mark-teal);
  }
  .brand-name {
    font-family: "Federo", sans-serif;
    font-size: 34px;
    color: var(--ink);
    letter-spacing: 1px;
  }
</style>
</head>
<body>
<main class="tote-print">
  <p class="quote-line quote-line--first">“There is only one race</p>
  <span class="quote-rule quote-rule--upper"></span>
  <p class="quote-line quote-line--second">the human race</p>
  <span class="quote-rule quote-rule--lower"></span>
  <p class="quote-line quote-line--third">and we all belong to it.”</p>

  <div class="brand-lockup">
    <span class="brand-dot"></span>
    <span class="brand-name">Every Road Meets Home</span>
  </div>
</main>
</body>
</html>
```